High-End Bifold Brochure for Aesthetics Medspa Business

I need a print-ready, bifold brochure designed for a high-end, luxurious Aesthetics/Medspa practice.

The brochure will showcase the latest IV Therapy content (6 options included in MENU.docx), and exclusive Vitamin B12+ wellness shot content (included in VB PDF). It should also include the business logo and basic office contact options.

The design should be clean, modern, and appealing with a light design. It should flow nicely and compliment the website theme/design. Preferably, having the 6 IV treatments inside bifold, with B12 shot on back/outside page. For easy viewing.

I have attached a few licensed images, if you think they will incorporate into the design nicely. Otherwise, please ignore them. If needed, I can send more.

https://velorabloomclinic.com/
Brand purple: #491c64
Fonts used on site:
Josefin Sans
Montserrat

Size should be 6.5 x 9 using specs on Quellpress's template page (Half Fold design)
https://www.quellpress.com/resources/templates

Font styles to use
Other font styles liked:
• Montserrat, Josefin Sans, or similar

Requirements
Must have
• Content included in MENU + B12 shot content on PDF.
Similar feel to the website, High-end, modern, luxurious

```html
<!DOCTYPE html>
<html lang="en">
<head>
<meta charset="utf-8">
<title>Velora Bloom Aesthetics – Bifold Brochure</title>
<link href="https://fonts.googleapis.com/css2?family=Montserrat:wght@300;400;600;700;800&family=Oswald:wght@600;700&family=Open+Sans:wght@400;600;700&family=Source+Sans+3:wght@400;600;700&display=swap" rel="stylesheet">
<style>
:root{
  --brand:#491c64;
  --brand-deep:#3d1554;
  --violet:#9a48cf;
  --ink:#1d1d1d;
  --page:#ffffff;
  --panel:#f2f2f2;
  --stage:#7e7e7e;
  --photo-dark:#120c09;
}
*{margin:0;padding:0;box-sizing:border-box}
html,body{width:1200px;height:800px;overflow:hidden;background:var(--stage)}
.page{position:absolute;top:56px;width:499px;height:688px;background:var(--page);overflow:hidden}
.cover{left:68px}
.inside{left:633px}

/* cover */
.cover-photo{position:absolute;left:0;top:0;width:499px;height:560px;
  background:radial-gradient(ellipse 42% 48% at 72% 58%, #c08a6e 0%, #8a5838 35%, transparent 70%),
             radial-gradient(ellipse 55% 60% at 55% 55%, #6b3f22 0%, #3a2213 50%, var(--photo-dark) 85%);}
.cover-shapes{position:absolute;left:0;top:0;width:499px;height:688px}
.cta-line{position:absolute;left:31px;color:#fff;line-height:1;white-space:nowrap}
.cta-call{top:49px;font:700 15px/1 Montserrat,sans-serif;letter-spacing:.5px}
.cta-for{top:67px;font:300 26px/1 Montserrat,sans-serif}
.cta-free{top:93px;font:700 57px/1 Oswald,sans-serif}
.cta-consult{top:150px;font:700 24px/1 Oswald,sans-serif}
.cta-phone{top:187px;left:32px;display:flex;align-items:center;gap:5px;background:var(--brand);width:161px;height:23px;padding-left:7px;font:700 16px/1 Montserrat,sans-serif}
.brand-name{position:absolute;left:296px;top:58px;display:flex;align-items:center;gap:8px;color:#fff;font:700 15px/1.2 Montserrat,sans-serif;letter-spacing:.5px}
.brand-dot{width:26px;height:26px;border-radius:50%;background:#fff;flex:none}
.bliss{position:absolute;left:36px;top:423px;width:132px;text-align:center;color:#fff;font:300 17px/19px Montserrat,sans-serif}
.bliss b{font-weight:600}
.contact{position:absolute;left:27px;top:543px;color:var(--ink);font:400 10.5px/1.3 Montserrat,sans-serif}
.contact h3{font:700 17px/1 Montserrat,sans-serif;color:var(--brand);letter-spacing:.3px}
.contact h3 span{font-weight:400}
.contact .rule{width:12px;height:2px;background:var(--brand);margin:4px 0 9px}
.contact-row{display:flex;gap:6px;align-items:flex-start;margin-bottom:5px}
.contact-row svg{flex:none;margin-top:2px}
.mini-name{position:absolute;left:170px;top:556px;color:var(--brand);font:700 11px/1.2 Montserrat,sans-serif;width:70px}
.tagline{position:absolute;left:250px;top:505px;width:249px;height:183px;background:var(--panel);color:var(--ink)}
.tag-line{position:absolute;left:0;width:249px;text-align:center;line-height:1;white-space:nowrap}
.tag-city{top:29px;font:300 27px/1 Montserrat,sans-serif;letter-spacing:1px}
.tag-premier{top:55px;font:800 38px/1 Montserrat,sans-serif;color:var(--brand);letter-spacing:2px}
.tag-medspa{top:90px;font:800 32px/1 Montserrat,sans-serif;color:var(--brand);letter-spacing:1px}
.tag-phone{position:absolute;left:31px;top:133px;width:188px;height:28px;background:var(--brand);display:flex;align-items:center;color:#fff;font:700 17px/1 Montserrat,sans-serif}
.tag-phone .icon{width:31px;height:28px;background:var(--violet);display:flex;align-items:center;justify-content:center;margin-right:10px;clip-path:polygon(0 0,80% 0,100% 50%,80% 100%,0 100%)}

/* inside */
.col-vitamins{position:absolute;left:0;top:0;width:250px;height:688px;background:#fbfbfb}
.col-iv{position:absolute;left:250px;top:0;width:249px;height:688px;background:var(--panel)}
.band{position:absolute;color:#fff;font:700 9.5px/1 "Open Sans",sans-serif;display:flex;align-items:center;padding-left:11px;white-space:nowrap}
.band-light{background:var(--violet);clip-path:polygon(0 0,93% 0,100% 100%,0 100%)}
.band-dark{background:var(--brand)}
.item{position:absolute;left:23px;width:203px;font:400 7.8px/10.7px "Source Sans 3",sans-serif;color:var(--ink);padding-left:9px;text-align:justify}
.item::before{content:"»";position:absolute;left:0;top:-1px;color:var(--brand);font-weight:700;font-size:9px}
.item b{color:var(--violet);font-weight:700}
.iv-title{position:absolute;left:22px;top:22px;width:210px;height:24px;background:var(--brand);color:#fff;font:700 18px/24px "Open Sans",sans-serif;padding-left:12px;white-space:nowrap}
.iv-sub{position:absolute;left:22px;top:46px;width:128px;height:22px;background:var(--violet);color:#fff;font:700 17px/22px "Open Sans",sans-serif;padding-left:12px;clip-path:polygon(0 0,100% 0,84% 100%,0 100%);white-space:nowrap}
.treat{position:absolute;left:22px;width:210px}
.treat h4{font:700 11px/14px "Source Sans 3",sans-serif;color:var(--violet);white-space:nowrap;letter-spacing:.2px}
.treat p{font:400 7.8px/10.2px "Source Sans 3",sans-serif;color:var(--ink);margin-top:4px}
.price{position:absolute;right:0;width:45px;height:14px;background:var(--brand-deep);color:#fff;font:700 10px/14px "Open Sans",sans-serif;text-align:right;padding-right:7px;clip-path:polygon(18% 0,100% 0,100% 100%,0 100%)}
.divider{position:absolute;left:22px;width:210px;height:1px;background:#8d6fa3}
</style>
</head>
<body>

<section class="page cover">
  <div class="cover-photo" role="img" aria-label="Portrait photograph of a woman with long curly auburn hair against a dark background"></div>
  <svg class="cover-shapes" viewBox="0 0 499 688" aria-hidden="true">
    <path d="M128,0 Q175,145 320,148 Q430,148 499,112" fill="none" stroke="#fff" stroke-width="1"/>
    <path d="M138,0 Q175,138 310,140 Q425,140 499,104 L499,0 Z" fill="#491c64"/>
    <path d="M0,385 Q150,480 300,507 Q420,520 499,492 L499,688 L0,688 Z" fill="#fff"/>
    <path d="M0,390 Q150,485 300,514 Q420,526 499,497" fill="none" stroke="#491c64" stroke-width="1.2"/>
    <circle cx="102" cy="459" r="69" fill="#fff"/>
    <circle cx="102" cy="459" r="66" fill="#491c64"/>
  </svg>

  <div class="cta-line cta-call">CALL TODAY</div>
  <div class="cta-line cta-for">FOR YOUR</div>
  <div class="cta-line cta-free">FREE</div>
  <div class="cta-line cta-consult">CONSULTATION</div>
  <div class="cta-line cta-phone">
    <svg width="14" height="14" viewBox="0 0 24 24"><circle cx="12" cy="12" r="10.5" fill="none" stroke="#fff" stroke-width="2"/><path d="M8.5 7c.6-.5 1.3-.4 1.6.2l.9 1.8c.2.5.1 1-.3 1.3l-.7.6c.6 1.3 1.6 2.4 2.9 3l.6-.7c.3-.4.9-.5 1.3-.3l1.8.9c.6.3.7 1 .2 1.6-1 1.1-2.4 1.3-3.9.5-2.2-1.2-3.8-2.9-4.9-5.1C7.3 9.3 7.5 8 8.5 7z" fill="#fff"/></svg>
    (520) 555-0187
  </div>

  <div class="brand-name"><span class="brand-dot"></span><span>VELORA BLOOM<br>&amp; AESTHETICS</span></div>

  <div class="bliss">Ready To<br><b>Experience</b><br>Aesthetic<br>Bliss?</div>

  <div class="contact">
    <h3>CONTACT <span>US</span></h3>
    <div class="rule"></div>
    <div class="contact-row">
      <svg width="7" height="9" viewBox="0 0 10 13"><path d="M5 0a4 4 0 0 1 4 4c0 3-4 8-4 8S1 7 1 4a4 4 0 0 1 4-4z" fill="none" stroke="#491c64" stroke-width="1.3"/><circle cx="5" cy="4" r="1.3" fill="#491c64"/></svg>
      <span>480 W Canyon Rise Rd<br>Suite 12<br>Tucson, Arizona 85704</span>
    </div>
    <div class="contact-row">
      <svg width="8" height="8" viewBox="0 0 24 24"><circle cx="12" cy="12" r="10" fill="none" stroke="#491c64" stroke-width="2.5"/><path d="M8.5 7c.6-.5 1.3-.4 1.6.2l.9 1.8c.2.5.1 1-.3 1.3l-.7.6c.6 1.3 1.6 2.4 2.9 3l.6-.7c.3-.4.9-.5 1.3-.3l1.8.9c.6.3.7 1 .2 1.6-1 1.1-2.4 1.3-3.9.5-2.2-1.2-3.8-2.9-4.9-5.1C7.3 9.3 7.5 8 8.5 7z" fill="#491c64"/></svg>
      <span>(520) 555-0187</span>
    </div>
    <div class="contact-row">
      <svg width="8" height="7" viewBox="0 0 12 9"><rect x=".5" y=".5" width="11" height="8" fill="none" stroke="#491c64"/><path d="M.5.5 6 5l5.5-4.5" fill="none" stroke="#491c64"/></svg>
      <span>info@velorabloomclinic.com</span>
    </div>
    <div class="contact-row">
      <svg width="8" height="8" viewBox="0 0 12 12"><circle cx="6" cy="6" r="5.3" fill="none" stroke="#491c64"/><ellipse cx="6" cy="6" rx="2.3" ry="5.3" fill="none" stroke="#491c64"/><path d="M.7 6h10.6" stroke="#491c64"/></svg>
      <span>www.velorabloomclinic.com</span>
    </div>
  </div>
  <div class="mini-name">VELORA BLOOM</div>

  <div class="tagline">
    <div class="tag-line tag-city">TUCSON'S</div>
    <div class="tag-line tag-premier">PREMIER</div>
    <div class="tag-line tag-medspa">MEDSPA</div>
    <div class="tag-phone">
      <span class="icon"><svg width="15" height="15" viewBox="0 0 24 24"><circle cx="12" cy="12" r="10.5" fill="none" stroke="#fff" stroke-width="2"/><path d="M8.5 7c.6-.5 1.3-.4 1.6.2l.9 1.8c.2.5.1 1-.3 1.3l-.7.6c.6 1.3 1.6 2.4 2.9 3l.6-.7c.3-.4.9-.5 1.3-.3l1.8.9c.6.3.7 1 .2 1.6-1 1.1-2.4 1.3-3.9.5-2.2-1.2-3.8-2.9-4.9-5.1C7.3 9.3 7.5 8 8.5 7z" fill="#fff"/></svg></span>
      (520) 555-0187
    </div>
  </div>
</section>

<section class="page inside">
  <div class="col-vitamins">
    <div class="band band-light" style="left:23px;top:22px;width:156px;height:19px">VITAMIN B12 COCKTAIL'S</div>
    <div class="band band-dark" style="left:23px;top:41px;width:204px;height:20px">ESSENTIAL VITAMINS &amp; NUTRIENTS:</div>

    <p class="item" style="top:78px"><b>Thiamine -</b> is used by the body to metabolize food for energy and maintain proper health and nerve function.</p>
    <p class="item" style="top:122px"><b>Riboflavin-</b> acts as an antioxidant within the body. Riboflavin prevents free radical damage and protects skin and eye health.</p>
    <p class="item" style="top:167px"><b>Nincinainide -</b> helps maintain a healthy cardiovascular system and metabolism, brain function, healthy skin formation, and aids in the prevention of and management of diabetes.</p>
    <p class="item" style="top:223px"><b>Pryridoxine -</b> is important for brain development and keeping the nervous and immune systems healthy.</p>
    <p class="item" style="top:258px"><b>Hydroxocobalamin -</b> helps with DNA synthesis and supports replication, it also helps in the body's use of fats and carbohydrates for energy, and in the making of new proteins.</p>
    <p class="item" style="top:314px"><b>Molhlonlne -</b> aids in tissue growth and repair, as well as promoting healthy hair, skin, and nails.</p>
    <p class="item" style="top:348px"><b>Inositol -</b> aids in the metabolic breakdown of fats, and helps reduce blood cholesterol.</p>
    <p class="item" style="top:382px"><b>L-carnitino -</b> helps convert fatty acids into energy.</p>
    <p class="item" style="top:406px"><b>Chromium -</b> helps move sugars from the blood system, and turn fats, carbs, and proteins into energy.</p>

    <div class="band band-light" style="left:23px;top:446px;width:145px;height:21px;font-size:10.5px">OVERALL BENEFITS:</div>

    <p class="item" style="top:482px">B12 helps aid in red blood cell formation and in DNA synthesis</p>
    <p class="item" style="top:511px">Aids in the healthy maintenance of the immune and nervous systems, and the optic nerve</p>
    <p class="item" style="top:541px">Helps improve skin tone, and strengthen nails and hair</p>
    <p class="item" style="top:569px">Boosts metabolism and energy (which may help reduce craving and encourage weight loss)</p>
    <p class="item" style="top:600px">Helps relieve cramping and bloating</p>
    <p class="item" style="top:620px">Improves memory (which may protect against Alzheimers)</p>
    <p class="item" style="top:649px">Enhances mood and lessons the effects of depression</p>
  </div>

  <div class="col-iv">
    <div class="iv-title">The Infusion Grove</div>
    <div class="iv-sub">IV THERAPY</div>

    <div class="treat" style="top:87px"><span class="price" style="top:-3px">$150</span><h4>IMMUNITY BOOSTER</h4>
      <p>Have a cold, flu or just need to give your immunity a boost? Let us mix a powerful punch in our booster bag just for you to prevent or relieve aches and pain</p></div>
    <div class="divider" style="top:146px"></div>

    <div class="treat" style="top:169px"><span class="price" style="top:-3px">$100</span><h4>REFRESH &amp; HYDRATE</h4>
      <p>Relieve dehydration from the extremes of lifestyle with our balanced electrolyte cocktail targeting jet lag, fatigue, stress and sports related activity to leave you feeling more youthful and refreshed!</p></div>
    <div class="divider" style="top:245px"></div>

    <div class="treat" style="top:259px"><span class="price" style="top:-3px">$150</span><h4>MIGRAINE BUSTER</h4>
      <p>Eradicate your migraine pain, nausea, vomiting, and light sensitivity with our magic formula</p></div>
    <div class="divider" style="top:309px"></div>

    <div class="treat" style="top:332px"><span class="price" style="top:-4px">$180</span><h4>WELLNESS INFUSION</h4>
      <p>This infusion of vitamins, minerals and electrolytes results in direct access of these nutrients into your cells, enhancing energy, decreasing stress and anxiety in addition to improving memory. Other benefits include relief of asthma, depression, allergies and fibromyalgia pain</p></div>
    <div class="divider" style="top:413px"></div>

    <div class="treat" style="top:436px"><span class="price" style="top:-3px">$200</span><h4>GLO</h4>
      <p>A Beauty mixture of Glutathione, Biotin and our special formula created to strengthen your hair, nails and skin for that SPECIAL LOOK!</p></div>
    <div class="divider" style="top:496px"></div>

    <div class="treat" style="top:512px"><span class="price" style="top:3px">$200</span><h4>THE ULTIMATE WEIGHT LOSS<br>INFUSION</h4>
      <p>Our unique fat burning formula targets fatty deposits resulting in fat expulsion from the body resulting in a more defined and contoured appearance.</p></div>
    <div class="divider" style="top:590px"></div>

    <div class="treat" style="top:606px"><span class="price" style="top:3px">$350</span><h4>NAD+ IV:<br>THE FOUNTAIN OF YOUTH (+-)</h4>
      <p>Anti-aging co-enzyme NAD+ in conjunction with Vitamins elevates brain health and beauty, all in one IV treatment!</p></div>
  </div>
</section>

</body>
</html>
```